Partlow Law Stationery - Letterhead, Envelopes, Business Cards

We need high quality business stationery for our Personal Injury Law Firm located in Houston, Texas. The design should include the logo, Partlow Law Group, PLLC, 713-555-0148, 2750 Marlowe Crescent, Suite 318, Houston, Texas 77099 www.PartlowLaw.example. The colors are blue and white. The letterhead should also include the Attorneys - Marcy Teague, Everett K. Partlow and Dorian Fisk.

```html
<!DOCTYPE html>
<html lang="en">
<head>
<meta charset="utf-8">
<title>Partlow Law Stationery</title>
<link href="https://fonts.googleapis.com/css2?family=Montserrat:wght@400;500;600;700&family=Noto+Sans:wght@400&display=swap" rel="stylesheet">
<style>
  :root{
    --navy:#0d1a3f;
    --white:#ffffff;
    --ink:#1b1b1b;
    --backdrop:#e4e4e4;
    --brand-font:"Montserrat", sans-serif;
    --body-font:"Noto Sans", sans-serif;
  }
  *{margin:0;padding:0;box-sizing:border-box}
  html,body{width:1200px;height:1200px;overflow:hidden}
  body{background:var(--backdrop);position:relative;font-family:var(--body-font);color:var(--ink)}

  /* Letterhead */
  .letterhead{position:absolute;left:218px;top:105px;width:765px;height:990px;background:var(--white)}
  .letterhead-header{position:absolute;left:0;top:0;width:765px;height:200px}
  .brand-mark{position:absolute;display:flex;align-items:center;justify-content:center;text-align:center;border:3px solid var(--white);border-radius:50%;background:var(--navy);color:var(--white);font-family:var(--brand-font);font-weight:700;line-height:1.1}
  .letterhead .brand-mark{left:65px;top:20px;width:130px;height:130px;font-size:19px}
  .brand-name{position:absolute;font-family:var(--brand-font);color:var(--white);white-space:nowrap}
  .brand-name .firm{display:block;font-weight:700;letter-spacing:.5px}
  .brand-name .practice{display:block;font-weight:400;letter-spacing:2.5px}
  .letterhead .brand-name{left:212px;top:68px}
  .letterhead .firm{font-size:25px}
  .letterhead .practice{font-size:18px;margin-top:2px}

  .letter-date{position:absolute;right:75px;top:201px;font-size:15px}
  .letter-body{position:absolute;left:78px;top:232px;width:600px;font-size:15px;line-height:33.2px}
  .letter-closing{margin-top:33px}

  .letterhead-footer{position:absolute;left:0;bottom:0;width:765px;height:103px;background:var(--navy);color:var(--white);font-family:var(--brand-font);font-size:12.5px}
  .attorney-list{position:absolute;left:78px;top:15px;list-style:none;line-height:18px}
  .attorney-list .label{font-weight:600}
  .contact-list{position:absolute;left:460px;top:15px;list-style:none}
  .contact-list li{display:flex;align-items:flex-start;gap:5px;line-height:12px;margin-bottom:9px}
  .contact-list svg{flex:none;margin-top:0}

  /* Business cards */
  .card{position:absolute;width:315px;height:180px}
  .card-front{left:825px;top:546px;background:var(--navy)}
  .card-front .brand-mark{left:111px;top:26px;width:90px;height:90px;font-size:13px;border-width:2px}
  .card-front .brand-name{left:0;width:315px;top:124px;text-align:center}
  .card-front .firm{font-size:13.5px}
  .card-front .practice{font-size:11px;letter-spacing:1.8px;margin-top:3px}

  .card-back{left:826px;top:759px;background:var(--white)}
  .card-back-band{position:absolute;left:0;top:0;width:315px;height:85px;background:var(--navy)}
  .card-back .brand-mark{left:38px;top:11px;width:64px;height:64px;font-size:9.5px;border-width:2px}
  .card-back .brand-name{left:110px;top:33px}
  .card-back .firm{font-size:11.5px}
  .card-back .practice{font-size:9px;letter-spacing:1.4px;margin-top:2px}
  .card-holder{position:absolute;left:98px;top:91px;font-family:var(--brand-font);font-size:12.5px;font-weight:600;color:var(--ink)}
  .card-contacts{position:absolute;left:98px;top:109px;list-style:none;font-family:var(--brand-font);font-size:9.2px;color:var(--navy)}
  .card-contacts li{display:flex;gap:4px;line-height:9.5px;margin-bottom:3.5px}
  .card-contacts svg{flex:none}
</style>
</head>
<body>

<section class="letterhead" aria-label="Letterhead">
  <svg class="letterhead-header" viewBox="0 0 765 200" aria-hidden="true">
    <polygon points="0,0 765,0 765,83 132,185 0,133" fill="var(--navy)"/>
    <polyline points="0,141 132,193 765,91" fill="none" stroke="var(--navy)" stroke-width="3"/>
  </svg>
  <div class="brand-mark">PARTLOW<br>LAW</div>
  <div class="brand-name">
    <span class="firm">PARTLOW LAW GROUP, PLLC</span>
    <span class="practice">INJURY ATTORNEYS</span>
  </div>

  <p class="letter-date">July 16, 2026</p>
  <div class="letter-body">
    <p>Dear Marcy,</p>
    <p>Thank you for inviting me to design your new letterhead.</p>
    <p>This letterhead is designed to embody simplicity, professionalism, and brand consistency. By using a clean layout with generous white space, the design ensures readability and a modern, uncluttered look. Your logo is placed prominently but tastefully, reinforcing brand recognition without overpowering the content. Professional sans serif typography<br>complements the contemporary style, ensuring that official<br>correspondence looks polished and credible.</p>
    <p>Overall, the design balances corporate sophistication<br>with the energetic, spirit that defines PARTLOW LAW.</p>
    <p>I hope you like it.</p>
    <p class="letter-closing">Best Regards,</p>
  </div>

  <footer class="letterhead-footer">
    <ul class="attorney-list">
      <li class="label">Attorneys</li>
      <li>Marcy Teague</li>
      <li>Everett K. Partlow</li>
      <li>Dorian Fisk</li>
    </ul>
    <ul class="contact-list">
      <li><svg width="12" height="12" viewBox="0 0 24 24"><path fill="#fff" d="M6.6 10.8a15 15 0 0 0 6.6 6.6l2.2-2.2c.3-.3.7-.4 1-.2 1.1.4 2.3.6 3.6.6.6 0 1 .4 1 1V20c0 .6-.4 1-1 1A17 17 0 0 1 3 4c0-.6.4-1 1-1h3.5c.6 0 1 .4 1 1 0 1.3.2 2.5.6 3.6.1.3 0 .7-.2 1z"/></svg>713-555-0148</li>
      <li><svg width="12" height="14" viewBox="0 0 24 28"><path fill="#fff" d="M12 0a9 9 0 0 0-9 9c0 7 9 19 9 19s9-12 9-19a9 9 0 0 0-9-9zm0 13a4 4 0 1 1 0-8 4 4 0 0 1 0 8z"/></svg><span>2750 Marlowe Crescent, Suite 318,<br>Houston, Texas 77099</span></li>
      <li><svg width="12" height="12" viewBox="0 0 24 24"><circle cx="12" cy="12" r="10" fill="none" stroke="#fff" stroke-width="2"/><path d="M2 12h20M12 2c3 3 3 17 0 20M12 2c-3 3-3 17 0 20" fill="none" stroke="#fff" stroke-width="1.6"/></svg>www.PartlowLaw.example</li>
    </ul>
  </footer>
</section>

<section class="card card-front" aria-label="Business card front">
  <div class="brand-mark">PARTLOW<br>LAW</div>
  <div class="brand-name">
    <span class="firm">PARTLOW LAW GROUP, PLLC</span>
    <span class="practice">INJURY ATTORNEYS</span>
  </div>
</section>

<section class="card card-back" aria-label="Business card back">
  <div class="card-back-band"></div>
  <div class="brand-mark">PARTLOW<br>LAW</div>
  <div class="brand-name">
    <span class="firm">PARTLOW LAW GROUP, PLLC</span>
    <span class="practice">INJURY ATTORNEYS</span>
  </div>
  <p class="card-holder">Marcy Teague</p>
  <ul class="card-contacts">
    <li><svg width="9" height="9" viewBox="0 0 24 24"><path fill="var(--navy)" d="M6.6 10.8a15 15 0 0 0 6.6 6.6l2.2-2.2c.3-.3.7-.4 1-.2 1.1.4 2.3.6 3.6.6.6 0 1 .4 1 1V20c0 .6-.4 1-1 1A17 17 0 0 1 3 4c0-.6.4-1 1-1h3.5c.6 0 1 .4 1 1 0 1.3.2 2.5.6 3.6.1.3 0 .7-.2 1z"/></svg>713-555-0148</li>
    <li><svg width="9" height="9" viewBox="0 0 24 24"><rect x="2" y="5" width="20" height="14" fill="var(--navy)"/><path d="M2 5l10 8 10-8" fill="none" stroke="#fff" stroke-width="2"/></svg>Marcy@PartlowLaw.example</li>
    <li><svg width="9" height="10" viewBox="0 0 24 28"><path fill="var(--navy)" d="M12 0a9 9 0 0 0-9 9c0 7 9 19 9 19s9-12 9-19a9 9 0 0 0-9-9zm0 13a4 4 0 1 1 0-8 4 4 0 0 1 0 8z"/></svg><span>2750 Marlowe Crescent, Suite 318,<br>Houston, Texas 77099</span></li>
    <li><svg width="9" height="9" viewBox="0 0 24 24"><circle cx="12" cy="12" r="10" fill="none" stroke="var(--navy)" stroke-width="2.4"/><path d="M2 12h20M12 2c3 3 3 17 0 20M12 2c-3 3-3 17 0 20" fill="none" stroke="var(--navy)" stroke-width="2"/></svg>www.PartlowLaw.example</li>
  </ul>
</section>

</body>
</html>
```